依頼詳細
【外貨両替】
外貨両替は学校へ出向いて行う、出張両替とご自宅へ外貨をお届けする外貨宅配の2プランがございます。どちらのプランにするかは学校の意向や参加者の規模や要望によります。

【フェリシオンクレスト】
外貨両替(現金)以外のお金としてトラベルマネーカード(フェリシオンクレスト)の紹介をしております。こちらはキャッシュレスに対応したカードで使い方はクレジットカードと同じですが、チャージした金額の範囲でご利用頂けるカードです。

今回、制作するパンフレットは旅行会社から旅行参加者へ配布してご質問等があれば旅行会社ではなく直接当社が窓口となり、旅行参加者からの質問等を受付いたします。
今回制作するパンフレットとは別に両替の申込書面、フェリシオンクレストの申込書面は別となります。あくまでも全体の案内、問い合わせ先の案内をするパンフレットです。
記載項目
資料を添付致しますので、要点をまとめてA4サイズカラー裏表で制作をお願い致します。
サイズ
A4
ページ数
両面
希望イメージ
シンプル 複雑
単色 カラフル
暗い 明るい
日常 高級
遊び心 厳粛
未来的 伝統的
女性的 男性的
希望する色
赤系、青系
納品ファイル
• イラストレーター形式 (.ai)
補足説明
■ 選んだ理由

社内で選考した結果、一番わかりやすく好評であった為当選とさせていただきました。

■ 提案者全員のお礼・コメント

この度は短期間でしたが、沢山の方にご参加頂き、またどの提案も良いものばかりでした。
また次回依頼する場合も宜しくお願い致します。

```html
<!DOCTYPE html>
<html lang="ja">
<head>
<meta charset="UTF-8">
<title>事前両替で海外研修もあんしん！</title>
<link href="https://fonts.googleapis.com/css2?family=M+PLUS+Rounded+1c:wght@500;700;800;900&family=Noto+Sans+JP:wght@400;500;700;900&display=swap" rel="stylesheet">
<style>
  :root {
    --sky: #e4f3fb;
    --sky-deep: #c9e6f5;
    --navy: #1f4f8f;
    --blue: #2f73c8;
    --blue-box: #2b6cb8;
    --ink: #2b2b2b;
    --yellow: #f7e27a;
    --yellow-edge: #e9c94a;
    --red: #d8312c;
    --pole: #d9b24a;
    --white: #ffffff;
  }
  * { margin: 0; padding: 0; box-sizing: border-box; }
  html, body { width: 846px; height: 1200px; overflow: hidden; }
  body {
    font-family: "Noto Sans JP", sans-serif;
    color: var(--ink);
    background: var(--white);
  }
  .flyer {
    position: relative;
    width: 846px;
    height: 1200px;
    background: linear-gradient(180deg, var(--sky) 0%, #f1f9fd 45%, var(--white) 100%);
    overflow: hidden;
  }
  .world-map {
    position: absolute; left: 40px; top: 20px; width: 770px; height: 300px;
    background: radial-gradient(ellipse at 50% 50%, var(--sky-deep) 0%, rgba(201,230,245,0) 70%);
    border-radius: 40%;
  }
  .art { position: absolute; }
  .art-plane { left: 610px; top: 40px; width: 200px; height: 80px; background: linear-gradient(90deg,#dfe9f2,#bcd0e2); border-radius: 40px 60px 30px 30px; }
  .art-suitcase { left: 708px; top: 232px; width: 92px; height: 112px; background: linear-gradient(180deg,#c7a57c,#a07e57); border-radius: 14px; }
  .art-person { left: 420px; top: 470px; width: 426px; height: 680px; background: linear-gradient(180deg,#f6dcc9 0%, #f2b9a4 40%, #8fb8df 100%); border-radius: 210px 210px 0 0; }
  .art-bus { left: 14px; top: 1000px; width: 200px; height: 150px; background: linear-gradient(180deg,#f0b2ad,#e07b74); border-radius: 18px; }

  .title {
    position: absolute; left: 0; right: 0; top: 52px; text-align: center;
    font-family: "M PLUS Rounded 1c", sans-serif; font-weight: 900;
    color: var(--navy); line-height: 1.12; letter-spacing: 2px;
  }
  .title-line { display: block; font-size: 84px; -webkit-text-stroke: 10px var(--white); paint-order: stroke fill; white-space: nowrap; }
  .title-line + .title-line { font-size: 76px; margin-top: 6px; }
  .title .small { font-size: 0.72em; color: var(--ink); }

  .intro { position: absolute; left: 52px; top: 278px; width: 640px; }
  .intro-head { display: flex; align-items: center; gap: 10px; font-family: "M PLUS Rounded 1c", sans-serif; font-weight: 800; font-size: 27px; color: var(--ink); margin-bottom: 10px; }
  .intro-head svg { width: 34px; height: 34px; }
  .intro-body { font-size: 15px; line-height: 1.62; font-weight: 500; }

  .merit { position: absolute; }
  .merit-flag { position: relative; height: 70px; display: flex; align-items: center; padding-left: 24px; }
  .merit-flag svg.flag-bg { position: absolute; left: 0; top: 0; width: 100%; height: 100%; }
  .merit-label { position: relative; font-family: "M PLUS Rounded 1c", sans-serif; font-weight: 900; font-size: 36px; color: var(--ink); white-space: nowrap; line-height: 1; }
  .merit-label .lead { color: var(--red); font-size: 54px; }
  .merit-note {
    margin: 8px 0 0 22px; background: var(--blue-box); color: var(--white);
    font-size: 13.5px; font-weight: 700; line-height: 1.5; padding: 8px 12px; border-radius: 4px;
  }
  .m1 { left: 40px; top: 452px; width: 380px; } .m1 .merit-note { width: 180px; }
  .m2 { left: 150px; top: 612px; width: 290px; } .m2 .merit-note { width: 180px; }
  .m3 { left: 40px; top: 762px; width: 350px; } .m3 .merit-note { width: 190px; }
  .m4 { left: 150px; top: 912px; width: 270px; } .m4 .merit-note { width: 180px; }

  .pole { position: absolute; width: 6px; background: var(--pole); border-radius: 3px; }

  .footer-note { position: absolute; right: 40px; bottom: 22px; font-size: 15px; font-weight: 500; }
</style>
</head>
<body>
<main class="flyer">
  <div class="world-map" role="img" aria-label="淡い水色の世界地図の背景"></div>
  <div class="art art-plane" role="img" aria-label="飛行機のイラスト"></div>
  <div class="art art-suitcase" role="img" aria-label="スーツケースのイラスト"></div>
  <div class="art art-person" role="img" aria-label="リュックを背負い指さしをする女性のイラスト"></div>
  <div class="art art-bus" role="img" aria-label="二階建てバスと時計塔のイラスト"></div>

  <h1 class="title">
    <span class="title-line">事前両替<span class="small">で</span></span>
    <span class="title-line">海外研修<span class="small">も</span>あんしん!</span>
  </h1>

  <section class="intro">
    <h2 class="intro-head">
      <svg viewBox="0 0 24 24" aria-hidden="true"><circle cx="12" cy="10" r="6" fill="#f7d24a"/><rect x="9" y="16" width="6" height="4" rx="1" fill="#888"/><path d="M12 1v2M3 10h2M19 10h2M5 4l1.5 1.5M19 4l-1.5 1.5" stroke="#f0b400" stroke-width="1.6" stroke-linecap="round"/></svg>
      知っていますか？
    </h2>
    <p class="intro-body">アフターコロナの現在、実は空港以外の市中の銀行窓口のほとんどが外貨両替をやめて、両替ができる場所が限られています。そこでおすすめなのが事前両替。国内で両替してから出発できるので、両替所を探す心配やトラブルになることもありません。事前に両替してから出発することで、海外研修を安心して迎えましょう！</p>
  </section>

  <div class="pole" style="left:40px;top:452px;height:300px"></div>
  <div class="pole" style="left:150px;top:612px;height:300px"></div>
  <div class="pole" style="left:40px;top:762px;height:300px"></div>
  <div class="pole" style="left:150px;top:912px;height:230px"></div>

  <section class="merit m1">
    <div class="merit-flag">
      <svg class="flag-bg" viewBox="0 0 100 20" preserveAspectRatio="none" aria-hidden="true"><polygon points="2,0 100,0 94,10 100,20 2,20" fill="#f7e27a" stroke="#e9c94a" stroke-width="0.5"/></svg>
      <span class="merit-label"><span class="lead">ゆ</span>とりができる！</span>
    </div>
    <p class="merit-note">事前両替で出発当日はゆとりを持って行動することができます！</p>
  </section>

  <section class="merit m2">
    <div class="merit-flag">
      <svg class="flag-bg" viewBox="0 0 100 20" preserveAspectRatio="none" aria-hidden="true"><polygon points="2,0 100,0 94,10 100,20 2,20" fill="#f7e27a" stroke="#e9c94a" stroke-width="0.5"/></svg>
      <span class="merit-label"><span class="lead">手</span>間なし！</span>
    </div>
    <p class="merit-note">外貨両替の取り扱い銀行へ出向く手間と手続きが省けます！</p>
  </section>

  <section class="merit m3">
    <div class="merit-flag">
      <svg class="flag-bg" viewBox="0 0 100 20" preserveAspectRatio="none" aria-hidden="true"><polygon points="2,0 100,0 94,10 100,20 2,20" fill="#f7e27a" stroke="#e9c94a" stroke-width="0.5"/></svg>
      <span class="merit-label"><span class="lead">使</span>いやすい！</span>
    </div>
    <p class="merit-note">小額紙幣を中心にパックしており現地での使い易さは抜群です！</p>
  </section>

  <section class="merit m4">
    <div class="merit-flag">
      <svg class="flag-bg" viewBox="0 0 100 20" preserveAspectRatio="none" aria-hidden="true"><polygon points="2,0 100,0 94,10 100,20 2,20" fill="#f7e27a" stroke="#e9c94a" stroke-width="0.5"/></svg>
      <span class="merit-label"><span class="lead">再</span>両替OK!</span>
    </div>
    <p class="merit-note">帰国後に余った紙幣は優遇レートにて日本円へ再両替が可能です！</p>
  </section>

  <p class="footer-note">詳しくは裏面をご覧ください。</p>
</main>
</body>
</html>
```